Creating a page for our Spanish tutoring service

We recently launched a new service and would like to create new "solutions" pages to add to our website.

Previously, we provided private one-on-one Spanish tutoring. Now, we are also providing group classes.

We have two documents with some basic copy on each offering. Our website is nice and does not require changes currently, but we do not have the internal bandwidth to build these pages. You would be using our existing design elements to build these two web pages.

Repurposing/copying blocks from our other pages is fine! We have a developer, so design only is required. If you do a good job on this first project, we will have many more pages and projects for you to do!

Our website is tutorlumo.com. TIA for any applicants.

---

Private classes copy:
https://files.quornbay.net/d/7kRtPw2mXa9vLq4ZsNe8Hb3uYc6Tf1Gd/view

Group classes copy:
https://files.quornbay.net/d/3pVxJh5nQe2WsKd8RmTa4YbLc9Uf7Zog/view

Target Market(s)

Online Spanish tutoring and online Spanish classes. We are a very high quality, yet affordable service. Our unique selling proposition is that we operate a completely remote team.

Current customers are typically well-to-do parents or professionals who want to learn Spanish for fun or personal development. They are usually in an okay standing financially (or want to be).

Those who pay for their kids to take lessons want them to have a better future or communicate with their families. Those who are young typically subscribe because they want a better future for themselves. Those who are 30+ years old learn for leisure, travel, or for ongoing professional development.

They want a quality product without paying the high costs associated with in-person tutoring, which is significantly more expensive. They also want to avoid cheaper solutions that are low cost but conversely low quality.

Number of Pages Required

2 page

Font styles to use
Other font styles liked:
• Avenir is our font

Requirements
Must have
• A look and feel consistent with the rest of our website.

```html
<!DOCTYPE html>
<html lang="en">
<head>
<meta charset="utf-8">
<title>TutorLumo – Online Spanish Tutoring</title>
<link rel="stylesheet" href="https://fonts.googleapis.com/css2?family=Nunito+Sans:wght@300;400;600;700;800&display=swap">
<style>
:root{
  --teal:#5fbfb3;
  --teal-dark:#36a596;
  --teal-band:#5bbbae;
  --orange:#f47b48;
  --ink:#3b3f44;
  --muted:#6a6f74;
  --gray-band:#efefef;
  --soft:#f3f6f7;
  --footer:#f8f4f2;
  --white:#ffffff;
  --review-green:#1fb37a;
}
*{margin:0;padding:0;box-sizing:border-box}
html,body{width:1200px;height:2769px;overflow:hidden}
body{font-family:"Nunito Sans",Arial,sans-serif;color:var(--ink);background:var(--white);position:relative}
.abs{position:absolute}
section{position:absolute;left:0;width:1200px}

/* hero */
.hero{top:0;height:475px;background:linear-gradient(100deg,#6cc3b8 0%,#76c8bd 45%,#9cd6cc 70%,#c6e6df 100%)}
.hero-photo{right:0;top:0;width:640px;height:475px;background:radial-gradient(ellipse at 65% 40%,rgba(240,230,220,.55),rgba(118,200,189,0) 60%)}
.brand{left:196px;top:22px;display:flex;align-items:center;gap:8px;color:var(--white);font-weight:800;font-size:19px;letter-spacing:1.5px}
.brand .dot{width:12px;height:12px;background:var(--orange);border-radius:50%}
.nav{left:524px;top:28px;display:flex;gap:22px;align-items:center}
.nav a{color:var(--white);font-size:10px;font-weight:700;text-decoration:none;letter-spacing:.3px}
.nav .cta{background:var(--orange);padding:5px 16px;border-radius:12px;margin-left:0}
.hero h1{left:196px;top:152px;width:420px;color:var(--white);font-weight:600;font-size:32px;line-height:37px}
.hero .lede{left:196px;top:234px;width:330px;color:var(--white);font-size:18px;line-height:22px;font-weight:400}
.btn{background:var(--orange);color:var(--white);font-size:8.5px;font-weight:800;letter-spacing:.6px;border-radius:12px;text-align:center;text-decoration:none}
.hero .btn{left:197px;top:301px;width:108px;height:22px;line-height:22px}

/* rating */
.rating{top:475px;height:69px;background:var(--gray-band)}
.rating .row{left:269px;top:22px;display:flex;align-items:center;gap:12px;font-size:14px}
.boxes{display:flex;gap:3px;margin:0 4px}
.boxes i{width:24px;height:24px;background:var(--review-green);display:block}
.rating b{font-weight:600}
.rating .muted{color:var(--muted)}
.review-brand{display:flex;align-items:center;gap:5px;font-weight:700;font-size:16px;margin-left:6px}
.review-brand span{width:14px;height:14px;border-radius:50%;background:var(--review-green)}

/* features */
.features{top:544px;height:278px}
.feature{top:70px;width:270px}
.feature svg{display:block;margin-left:5px}
.feature h3{margin-top:16px;color:var(--teal-dark);font-weight:400;font-size:17px;letter-spacing:.2px}
.feature p{margin-top:9px;font-size:9.5px;line-height:15px;color:var(--muted);padding-left:2px;width:230px}
.divider{top:62px;width:1px;height:150px;background:#e3e3e3}

/* why */
.why{top:822px;height:466px;background:var(--soft)}
.why-photo{right:0;top:0;width:555px;height:466px;background:linear-gradient(90deg,rgba(243,246,247,1) 0%,#e4dbd2 30%,#d9cfc6 60%,#ece7e2 100%)}
.why h2{left:197px;top:105px;font-weight:400;font-size:30px;color:var(--ink)}
.why .intro{left:197px;top:156px;width:370px;font-size:10px;line-height:15px}
.why h3{left:197px;top:225px;color:var(--teal-dark);font-weight:600;font-size:20px}
.kind{top:262px;width:215px}
.kind .title{display:flex;align-items:center;gap:8px;font-size:17px}
.kind p{margin-top:8px;font-size:9px;line-height:11.5px;color:var(--muted)}

/* reasons */
.reasons{top:1288px;height:655px}
.reasons h2{left:243px;top:58px;width:370px;font-weight:700;font-size:19px;line-height:29px;color:var(--ink)}
.reason .num{left:201px;width:31px;height:31px;border-radius:50%;background:var(--teal-dark);color:var(--white);font-size:12px;font-weight:700;text-align:center;line-height:31px}
.reason h3{left:240px;color:var(--teal-dark);font-weight:600;font-size:17px}
.reason p{left:240px;width:346px;font-size:10.5px;line-height:17.6px;color:var(--muted);font-weight:600}
.tablet{left:602px;top:45px;width:344px;height:610px;background:linear-gradient(180deg,rgba(255,255,255,0) 0%,#eef6f4 20%,#d8eeea 55%,#f0d9cb 100%);border-radius:4px}

/* testimonials */
.testimonials{top:1943px;height:426px;background:var(--soft)}
.video-frame{left:258px;top:92px;width:331px;height:239px;background:var(--teal)}
.video{left:249px;top:103px;width:331px;height:234px;background:linear-gradient(180deg,#5b6470,#8f8a87 55%,#3f4a57)}
.play{left:390px;top:210px;width:52px;height:52px;border-radius:50%;background:rgba(60,50,45,.7)}
.play svg{position:absolute;left:19px;top:15px}
.arrow{top:197px}
.testimonials h2{left:656px;top:110px;font-weight:400;font-size:30px}
.testimonials blockquote{left:656px;top:164px;width:300px;font-size:11.3px;line-height:19.5px;color:var(--muted)}
.testimonials .name{left:656px;top:270px;color:var(--teal);font-size:16px}
.testimonials .role{left:655px;top:290px;font-size:11px}

/* group */
.group{top:2369px;height:145px;background:var(--teal-band);color:var(--white)}
.group h2{left:249px;top:30px;font-weight:400;font-size:30px;line-height:33px}
.group p{left:250px;top:100px;width:390px;font-size:10px;line-height:15.5px}
.group .btn{left:746px;top:53px;width:191px;height:28px;line-height:28px}

/* footer */
.footer{top:2514px;height:255px;background:var(--footer)}
.fcol{top:56px}
.fcol h4{font-size:11.5px;font-weight:600;color:var(--ink);margin-bottom:6px}
.fcol a{display:block;font-size:10px;color:var(--muted);text-decoration:none;line-height:16px}
.social{left:852px;top:121px;display:flex;gap:7px}
.social span{width:20px;height:20px;border-radius:50%;display:block}
.copyright{left:384px;top:191px;display:flex;align-items:center;gap:8px;font-size:8.5px;color:var(--muted)}
.copyright .mini{display:flex;align-items:center;gap:4px;color:var(--teal-dark);font-weight:800;font-size:11px;letter-spacing:1px}
.copyright .mini i{width:7px;height:7px;border-radius:50%;background:var(--orange);display:block}
.copyright u{color:#3a3acb}
</style>
</head>
<body>

<section class="hero">
  <div class="abs hero-photo" role="img" aria-label="Smiling woman with glasses studying on a laptop"></div>
  <div class="abs brand">TUTORLUMO <span class="dot"></span></div>
  <nav class="abs nav">
    <a href="#">HOW IT WORKS</a><a href="#">TEACHERS</a><a href="#">TESTIMONIALS</a><a href="#">PRICING</a><a href="#">ABOUT US</a><a href="#" class="cta">GET STARTED</a>
  </nav>
  <h1 class="abs">Award-Winning Online Spanish Tutoring</h1>
  <p class="abs lede">Learn fast and effectively with fun and engaging private Spanish classes</p>
  <a class="abs btn" href="#">TRY A FREE CLASS</a>
</section>

<section class="rating">
  <div class="abs row">
    <span>Our Customers Say</span>
    <b style="margin-left:6px">Excellent</b>
    <div class="boxes"><i></i><i></i><i></i><i></i><i></i></div>
    <span><b>4.9</b> <span class="muted">out of 5 based on</span> <b>2,519</b> reviews</span>
    <span class="review-brand"><span></span>ReviewNest</span>
  </div>
</section>

<section class="features">
  <div class="abs feature" style="left:195px">
    <svg width="40" height="34" viewBox="0 0 40 34" fill="none" stroke="#5fbfb3" stroke-width="1.4"><circle cx="20" cy="8" r="5"/><circle cx="9" cy="13" r="4"/><circle cx="31" cy="13" r="4"/><path d="M10 30c0-7 4-11 10-11s10 4 10 11z"/><path d="M2 31c0-6 3-9 7-9M38 31c0-6-3-9-7-9"/></svg>
    <h3>EXPERT TEACHERS</h3>
    <p>TutorLumo teachers are trained in the science of teaching Spanish and have worked thousands of hours helping Spanish learners globally.</p>
  </div>
  <div class="abs divider" style="left:449px"></div>
  <div class="abs feature" style="left:485px">
    <svg width="34" height="34" viewBox="0 0 34 34" fill="none" stroke="#5fbfb3" stroke-width="1.4"><rect x="2" y="2" width="30" height="30"/><path d="M2 9h30"/><rect x="6" y="13" width="22" height="6"/><path d="M6 24h10M6 28h10M20 24h8M20 28h8"/></svg>
    <h3>DEDICATED ATTENTION</h3>
    <p>Accelerate your learning with one-on-one classes featuring a curriculum that's custom built for your unique needs and interests</p>
  </div>
  <div class="abs divider" style="left:740px"></div>
  <div class="abs feature" style="left:772px">
    <svg width="28" height="36" viewBox="0 0 28 36" fill="none" stroke="#5fbfb3" stroke-width="1.4"><path d="M10 14V5a2 2 0 0 1 4 0v12l2-1a2 2 0 0 1 3 1l1 1 3 1v10l-3 5H10l-5-9 2-2 3 3z"/><path d="M5 4l2 2M19 4l-2 2M12 0v2"/></svg>
    <h3>FLEXIBLE AND CONVENIENT</h3>
    <p>Online tutoring allows you to learn whenever, and wherever. Find time to continue learning, even if you have a tight schedule.</p>
  </div>
</section>

<section class="why">
  <div class="abs why-photo" role="img" aria-label="Woman with curly hair taking notes beside a laptop"></div>
  <h2 class="abs">Why Private Spanish Tutoring?</h2>
  <p class="abs intro">Fast-track your language learning using online Spanish classes with a dedicated teacher. Get an effective curriculum that's built around your specific goals and current level of comprehension.</p>
  <h3 class="abs">What kinds of classes can you expect?</h3>
  <div class="abs kind" style="left:197px">
    <div class="title"><svg width="32" height="26" viewBox="0 0 32 26" fill="none" stroke="#5fbfb3" stroke-width="1.3"><path d="M1 1h20v13H9l-5 4v-4H1z"/><path d="M14 17v3h10l5 4v-4h2V8h-6"/></svg>Conversational</div>
    <p>Want to get ready for conversations in the real world? Lessons on every-day topics can help build your vocabulary in essential areas and help you build more confidence speaking.</p>
  </div>
  <div class="abs kind" style="left:435px">
    <div class="title"><svg width="26" height="26" viewBox="0 0 26 26" fill="none" stroke="#5fbfb3" stroke-width="1.3"><path d="M2 24L11 2l9 22M6 15h10"/><path d="M14 24l4-4 6-8"/></svg>Grammar</div>
    <p>Learn the basics or perfect your grammar for use in personal or professional settings. Our grammar-oriented lessons will build you vocabulary while helping you speak perfectly like a native.</p>
  </div>
</section>

<section class="reasons">
  <h2 class="abs">3 reasons why TutorLumo is perfect for your child.</h2>
  <div class="reason">
    <div class="abs num" style="top:121px">1</div>
    <h3 class="abs" style="top:124px">Distance learning.</h3>
    <p class="abs" style="top:166px">Every child should have access to effective educators. Our online classes ensure they never lose that privilege. Plus, our offices are based in Colombia, which allows us to offer a more cost-effective solution. Don't settle for a less than stellar teacher for your child due to geographic or financial constraints.</p>
  </div>
  <div class="reason">
    <div class="abs num" style="top:283px">2</div>
    <h3 class="abs" style="top:286px">Personalized curriculum.</h3>
    <p class="abs" style="top:327px">Public classrooms are crammed with students. Not getting enough individual attention is the single biggest reason why students are not successful. Our 1:1 program allows for teachers to really understand your child; so that they can build lessons and activities around their unique learning style, strengths, and interests.</p>
  </div>
  <div class="reason">
    <div class="abs num" style="top:444px">3</div>
    <h3 class="abs" style="top:447px">Ongoing assessment.</h3>
    <p class="abs" style="top:489px">We conduct regular assessments to provide you with updates on your child's improving comprehension in the language. Not only will your child have access to a world class teacher. They'll also be assigned a member of our Student Success team to help monitor and report back to you on progress and tweaks made to speed up the learning process.</p>
  </div>
  <div class="abs tablet" role="img" aria-label="Hand holding a tablet showing an illustrated family members vocabulary lesson"></div>
</section>

<section class="testimonials">
  <svg class="abs arrow" style="left:162px" width="14" height="24" viewBox="0 0 14 24" fill="none" stroke="#555" stroke-width="2"><path d="M12 2L2 12l10 10"/></svg>
  <svg class="abs arrow" style="left:1012px" width="14" height="24" viewBox="0 0 14 24" fill="none" stroke="#555" stroke-width="2"><path d="M2 2l10 10L2 22"/></svg>
  <div class="abs video-frame"></div>
  <div class="abs video" role="img" aria-label="Video testimonial from a student"></div>
  <div class="abs play"><svg width="18" height="22" viewBox="0 0 18 22" fill="none" stroke="#fff" stroke-width="1.5"><path d="M1 1l16 10L1 21z"/></svg></div>
  <h2 class="abs">What our students say</h2>
  <blockquote class="abs">"The main things to note are the availability and patience of the teachers. Having them available pretty much on standby, and willing to work with me at my speed, ensured a really got enough practice with each subject to feel comfortable before moving on."</blockquote>
  <div class="abs name">Daniel Hartley</div>
  <div class="abs role">Learning to socialize</div>
</section>

<section class="group">
  <h2 class="abs">Group classes are also available<br>OR Try group classes instead</h2>
  <p class="abs">Led by our certified teachers, group classes give learners the opportunity to have real, interactive conversations in Spanish with their peers.</p>
  <a class="abs btn" href="#">LEARN MORE ABOUT GROUP CLASSES</a>
</section>

<footer class="footer" style="position:absolute;left:0;width:1200px">
  <div class="abs fcol" style="left:248px"><h4>Information</h4><a href="#">How It Works</a><a href="#">Pricing</a></div>
  <div class="abs fcol" style="left:369px"><h4>Service</h4><a href="#">Teachers</a><a href="#">Testimonials</a></div>
  <div class="abs fcol" style="left:490px"><h4>Company</h4><a href="#">About Us</a><a href="#">Partner Program</a></div>
  <div class="abs fcol" style="left:611px"><h4>Legal</h4><a href="#">Privacy policy</a><a href="#">Terms of use</a></div>
  <div class="abs fcol" style="left:853px;top:69px"><h4>Get in touch</h4><a href="#">Contact Support</a></div>
  <div class="abs social"><span style="background:#3b5a9a"></span><span style="background:#d92b2b"></span><span style="background:#c9357f"></span></div>
  <div class="abs copyright"><span class="mini">TUTORLUMO <i></i></span><span>Copyright © 2020 TutorLumo, Inc. All rights reserved. <u>Privacy Policy</u>. Terms &amp; Conditions.</span></div>
</footer>

</body>
</html>
```